BIX Promotional flyer for students

We're looking for an 8.5" x 11" flyer that will be distributed to schools. Please see language to include in attached files.

Target Market(s)

The parents and teachers of high school students

Industry/Entity Type

Mental health

Other font styles liked:
• Monserrat and Roboto Slab

Requirements
Must have
• See attached pdf for language to be included on the flyer. Please use the color palette from our website: www.bixzone.tv. Please include some imagery of students. Please ensure the
Nice to have
• Feel free to use any of the graphics provided. See our website for our brand look & feel: www.bixzone.tv

```html
<!DOCTYPE html>
<html lang="en">
<head>
<meta charset="UTF-8">
<title>BIX Fundraising Flyer</title>
<link href="https://fonts.googleapis.com/css2?family=Montserrat:wght@400;700;800&display=swap" rel="stylesheet">
<style>
  :root {
    --stage: #d6d6d6;
    --blue-top: #167cc5;
    --blue-bottom: #0a5ca6;
    --orange: #f47330;
    --white: #ffffff;
    --ink: #1b1b1b;
  }
  * { margin: 0; padding: 0; box-sizing: border-box; }
  html, body {
    width: 1040px; height: 1200px; overflow: hidden;
    background: var(--stage);
    font-family: 'Montserrat', Arial, sans-serif;
  }
  .flyer {
    position: absolute; left: 56px; top: 0;
    width: 927px; height: 1200px; overflow: hidden;
    background: linear-gradient(180deg, var(--blue-top) 0%, var(--blue-bottom) 100%);
    color: var(--white);
  }
  .badge { position: absolute; left: 0; top: 0; width: 927px; height: 760px; }
  .badge text { font-family: 'Montserrat', Arial, sans-serif; font-weight: 700; fill: var(--white); }
  .students-photo {
    position: absolute; left: 430px; top: 770px; width: 497px; height: 430px;
    background: linear-gradient(160deg, #c9c2bb 0%, #b9b1a8 35%, #f08a45 55%, #7a2a30 80%, #4a2a24 100%);
    border-radius: 220px 220px 0 0;
    opacity: 0.9;
  }
  .headline {
    position: absolute; left: 53px; top: 760px;
    font-weight: 700; font-size: 40px; line-height: 44px; letter-spacing: 0.5px;
  }
  .headline .accent { color: var(--orange); }
  .intro {
    position: absolute; left: 53px; top: 916px; width: 340px;
    font-size: 17px; line-height: 24.3px; font-weight: 400;
  }
  .intro strong { font-weight: 700; }
  .web-band { position: absolute; left: 0; top: 1090px; width: 420px; height: 80px; }
  .web-band text { font-family: 'Montserrat', Arial, sans-serif; }
</style>
</head>
<body>
  <main class="flyer">
    <svg class="badge" viewBox="0 0 927 760" aria-label="Fundraise with BIX — 50% of all proceeds go back to your school">
      <defs>
        <path id="arc-top" d="M 242 381 A 221 221 0 0 1 684 381"/>
        <path id="arc-inner" d="M 202 381 A 261 261 0 0 0 724 381"/>
        <path id="arc-outer" d="M 162 381 A 301 301 0 0 0 764 381"/>
      </defs>
      <circle cx="463" cy="381" r="330" fill="none" stroke="var(--white)" stroke-width="1.5"/>
      <circle cx="463" cy="381" r="202" fill="var(--orange)"/>
      <text x="463" y="420" text-anchor="middle" font-size="150" font-weight="800" letter-spacing="-4">bix</text>
      <text font-size="60" letter-spacing="3">
        <textPath href="#arc-top" startOffset="50%" text-anchor="middle">FUNDRAISE WITH</textPath>
      </text>
      <text font-size="31" letter-spacing="1">
        <textPath href="#arc-inner" startOffset="50%" text-anchor="middle">50% OF ALL PROCEEDS</textPath>
      </text>
      <text font-size="31" letter-spacing="1">
        <textPath href="#arc-outer" startOffset="50%" text-anchor="middle">GO BACK TO YOUR SCHOOL</textPath>
      </text>
    </svg>

    <div class="students-photo" role="img" aria-label="Photo of two smiling high school students, one holding an orange folder, one wearing a backpack"></div>

    <h1 class="headline">SUPPORT THE<br><span class="accent">MENTAL HEALTH</span><br>OF YOUR STUDENTS</h1>

    <p class="intro"><strong>BIX</strong> is a simple and effective way to improve mental health. Your students will learn valuable coping skills and techniques from expert clinicians who analyze real cases and share their insights and advice.</p>

    <svg class="web-band" viewBox="0 0 420 80" aria-label="BIXZONE.TV">
      <polygon points="0,19 392,19 359,56 0,56" fill="var(--white)"/>
      <circle cx="95" cy="37" r="36" fill="var(--orange)"/>
      <text x="95" y="46" text-anchor="middle" font-size="27" font-weight="700" fill="var(--white)">bix</text>
      <text x="150" y="45" font-size="21" font-weight="800" fill="var(--ink)">BIXZONE.TV</text>
    </svg>
  </main>
</body>
</html>
```